Classic wrap

Looking for sharp eye catching colors for HVAC.Looking for different and easy to spot

Target Market(s)

HVAC

Requirements
Must have
• eye catching colors Blue and yellow
Nice to have
• HEATING- AIR CONDITIONING
Emergency Service

```html
<!DOCTYPE html>
<html lang="en">
<head>
<meta charset="utf-8">
<title>Brightline Home Services – Van Wrap</title>
<link href="https://fonts.googleapis.com/css2?family=Oswald:wght@500&family=Poppins:wght@500;700;800&display=swap" rel="stylesheet">
<style>
  :root {
    --sky: #36b3e5;
    --sky-light: #7fd4f4;
    --sky-seam: #1d7fab;
    --band: #141518;
    --trim: #1b1c1f;
    --glass: #d3d5d8;
    --glass-dark: #25282c;
    --tire: #191919;
    --ink: #111214;
    --white: #ffffff;
    --sun: #ffd21f;
    --ice: #6cc7ee;
    --flame: #d8262c;
    --navy: #1e4e7a;
    --tail: #b3161d;
    --chrome: #9ea3a8;
    --page: #ffffff;
  }
  html, body {
    margin: 0;
    padding: 0;
    width: 1200px;
    height: 1200px;
    overflow: hidden;
    background: var(--page);
  }
  .wrap-canvas { display: block; width: 1200px; height: 1200px; }
  .service-label { font-family: "Oswald", sans-serif; font-weight: 500; font-size: 15px; fill: var(--white); }
  .phone { font-family: "Poppins", sans-serif; font-weight: 700; font-size: 19px; fill: var(--ink); }
  .web { font-family: "Poppins", sans-serif; font-weight: 500; font-size: 13.5px; fill: var(--ink); }
  .brand-name { font-family: "Poppins", sans-serif; font-weight: 800; fill: var(--sun); }
</style>
</head>
<body>
<svg class="wrap-canvas" viewBox="0 0 960 960" xmlns="http://www.w3.org/2000/svg">
  <defs>
    <radialGradient id="burst" cx="0.5" cy="0.45" r="0.65">
      <stop offset="0" stop-color="var(--sky-light)"/>
      <stop offset="1" stop-color="var(--sky)"/>
    </radialGradient>
    <radialGradient id="hubcap" cx="0.45" cy="0.4" r="0.6">
      <stop offset="0" stop-color="#eef0f2"/>
      <stop offset="1" stop-color="#979da3"/>
    </radialGradient>
  </defs>

  <ellipse class="ground-shadow" cx="470" cy="630" rx="440" ry="12" fill="#000" opacity="0.14"/>

  <!-- body -->
  <path class="van-body" d="M25 560 L28 470 Q32 452 55 446 L170 418 Q205 380 255 330 Q290 290 340 268 Q365 258 400 257 L880 254 Q912 254 916 285 L922 520 L922 560 Z" fill="url(#burst)"/>

  <!-- upper black band -->
  <path class="side-band" d="M262 320 L900 316 L920 318 L920 420 L186 420 L200 400 Z" fill="var(--band)"/>
  <line x1="186" y1="421" x2="920" y2="421" stroke="var(--chrome)" stroke-width="2"/>

  <!-- hood -->
  <path class="hood" d="M28 468 Q32 452 55 446 L170 418 L200 416 L196 440 L110 450 L28 464 Z" fill="var(--band)"/>

  <!-- windshield edge and side window -->
  <path class="windshield" d="M176 416 Q215 370 262 322 L280 320 Q232 370 200 414 Z" fill="var(--glass-dark)"/>
  <path class="side-window" d="M205 428 L210 378 Q214 348 240 342 L348 330 L350 430 Z" fill="var(--glass)" stroke="var(--trim)" stroke-width="4"/>
  <rect class="mirror" x="188" y="398" width="14" height="26" rx="3" fill="var(--trim)"/>

  <!-- lower band, sill stripe, bumper -->
  <rect class="lower-band" x="25" y="508" width="897" height="57" fill="var(--band)"/>
  <rect class="sill-stripe" x="245" y="565" width="420" height="8" fill="var(--sky)"/>
  <path class="sill" d="M25 565 L245 565 L245 573 L665 573 L665 565 L922 565 L922 582 L25 582 Z" fill="var(--band)"/>
  <path class="bumper" d="M25 515 L70 512 L70 586 L25 586 Z" fill="var(--trim)"/>

  <!-- seams & handle -->
  <g class="seams" stroke="var(--sky-seam)" stroke-width="1.4" fill="none" opacity="0.75">
    <line x1="355" y1="262" x2="355" y2="580"/>
    <line x1="380" y1="260" x2="380" y2="580"/>
    <line x1="605" y1="256" x2="605" y2="580"/>
  </g>
  <rect class="handle" x="328" y="438" width="22" height="6" rx="2" fill="var(--trim)"/>

  <!-- lights -->
  <path class="headlight" d="M46 460 L112 446 L114 470 L52 484 Z" fill="#e2e5e8" stroke="var(--trim)" stroke-width="2"/>
  <rect class="taillight" x="894" y="410" width="18" height="96" rx="4" fill="var(--tail)"/>

  <!-- wheel arches and wheels -->
  <path class="arch" d="M106 586 A66 66 0 0 1 238 586 Z" fill="var(--band)"/>
  <path class="arch" d="M686 586 A66 66 0 0 1 818 586 Z" fill="var(--band)"/>
  <g class="wheel">
    <circle cx="172" cy="586" r="54" fill="var(--tire)"/>
    <circle cx="172" cy="586" r="36" fill="url(#hubcap)"/>
    <circle cx="172" cy="586" r="8" fill="#7d838a"/>
  </g>
  <g class="wheel">
    <circle cx="752" cy="586" r="54" fill="var(--tire)"/>
    <circle cx="752" cy="586" r="36" fill="url(#hubcap)"/>
    <circle cx="752" cy="586" r="8" fill="#7d838a"/>
  </g>

  <!-- brand name -->
  <g class="brand">
    <text class="brand-name" x="493" y="432" font-size="36" text-anchor="middle">BRIGHTLINE</text>
    <text class="brand-name" x="493" y="456" font-size="14" text-anchor="middle">HOME SERVICES</text>
  </g>

  <!-- services -->
  <g class="services">
    <circle cx="660" cy="334" r="12" fill="var(--ice)"/>
    <g stroke="var(--white)" stroke-width="1.8" stroke-linecap="round">
      <line x1="660" y1="326" x2="660" y2="342"/>
      <line x1="653" y1="330" x2="667" y2="338"/>
      <line x1="653" y1="338" x2="667" y2="330"/>
    </g>
    <text class="service-label" x="687" y="340">AIR CONDITIONING &amp; COOLING</text>

    <circle cx="660" cy="368" r="12" fill="var(--flame)"/>
    <path d="M660 359 Q667 366 665 371 Q664 376 660 376 Q655 376 655 371 Q655 366 660 359 Z" fill="var(--white)"/>
    <text class="service-label" x="687" y="374">HEATING &amp; FURNACES</text>

    <circle cx="660" cy="402" r="12" fill="var(--navy)"/>
    <rect x="653" y="396" width="14" height="11" rx="1" fill="none" stroke="var(--white)" stroke-width="1.6"/>
    <text class="service-label" x="687" y="408">AIR DUCTS</text>
  </g>

  <!-- contact -->
  <text class="phone" x="205" y="474">718-555-0142</text>
  <text class="web" x="628" y="457">www.brightlinehvacnyc.com</text>
</svg>
</body>
</html>
```